Cryptocurrency Advisor Business Card

Dravelin Consulting Services is my company, which advises many projects in the ICO/Cryptocurrency industry. I'd like to get a sleek, preferably matte black or matte dark blue finish, business card with the company name (and simple logo w/ crypto feel) on one side and while the other side I'd like a small twitter and telegram logo together maybe separated by a / as it's the same, then an email and a phone logo so I can insert those specifics there (no address). Can have name then CEO section too. At the bottom of that section, find a place for more of a job description: ICO Advisor, World Champion Gamer, Esports Award Winner, Quorvane Expert. You can possibly design a simple logo or use something with a crypto twist or background, but nothing too complex. Rounded edges for printing not square.
Updates

Had personal issues taking a few days away from me being able to provide feedback and check designs, etc. Will be more active now finalizing design just needed few days from issue but all is sorted.

Target Market(s)

Cryptocurrency industry

Industry/Entity Type

Management Consulting

Contact Information for Business Card

Font styles to use
Sans Serif

Colors
5c5c5c
474747
757575
9d9d9d
aaaaaa
333333
0355a3

Requirements
Must have
• Refer to Details/Description
Nice to have
Should not have
• Address section

```html
<!DOCTYPE html>
<html lang="en">
<head>
<meta charset="utf-8">
<title>Dravelin Consulting Services – Business Card</title>
<link rel="stylesheet" href="https://fonts.googleapis.com/css2?family=Arimo:wght@400;700&display=swap">
<style>
  :root {
    --brand-blue: #0355a3;
    --ink-dark: #333333;
    --grey-1: #474747;
    --grey-2: #5c5c5c;
    --grey-3: #757575;
    --grey-4: #9d9d9d;
    --grey-5: #aaaaaa;
    --stage: #e9e9e9;
    --card-black: #1e1f21;
  }
  * { box-sizing: border-box; margin: 0; padding: 0; }
  html, body { width: 1200px; height: 797px; overflow: hidden; }
  body {
    background: var(--stage);
    font-family: "Arimo", Arial, sans-serif;
    position: relative;
  }
  .card {
    position: absolute;
    top: 244px;
    width: 540px;
    height: 309px;
    border-radius: 24px;
    overflow: hidden;
    box-shadow: 0 8px 22px rgba(0,0,0,0.18);
  }
  /* Back side */
  .card-back {
    left: 40px;
    background: linear-gradient(160deg, #2a2b2e 0%, var(--card-black) 60%, #161719 100%);
    display: flex;
    flex-direction: column;
    align-items: center;
    justify-content: center;
  }
  .back-wordmark {
    color: var(--brand-blue);
    font-weight: 700;
    font-size: 64px;
    letter-spacing: 2px;
    line-height: 1;
  }
  .back-tagline {
    color: var(--brand-blue);
    font-weight: 400;
    font-size: 14px;
    margin-top: 10px;
    letter-spacing: 0.5px;
  }
  /* Front side */
  .card-front {
    left: 620px;
    background: linear-gradient(150deg, #e4e4e4 0%, #cfcfcf 45%, var(--grey-5) 100%);
  }
  .front-watermark {
    position: absolute;
    left: 10px;
    top: 70px;
    font-weight: 700;
    font-size: 150px;
    color: rgba(255,255,255,0.35);
    letter-spacing: 4px;
    line-height: 1;
    white-space: nowrap;
  }
  .front-brand {
    position: absolute;
    left: 24px;
    top: 118px;
    width: 180px;
  }
  .front-brand .wordmark {
    color: var(--brand-blue);
    font-weight: 700;
    font-size: 34px;
    line-height: 1;
  }
  .front-brand .tagline {
    color: var(--brand-blue);
    font-size: 11px;
    margin-top: 6px;
  }
  .divider {
    position: absolute;
    left: 214px;
    top: 30px;
    width: 2px;
    height: 250px;
    background: var(--brand-blue);
  }
  .details {
    position: absolute;
    left: 232px;
    top: 28px;
    right: 16px;
  }
  .person-name {
    color: var(--brand-blue);
    font-weight: 700;
    font-size: 24px;
  }
  .roles {
    list-style: none;
    margin-top: 4px;
    color: var(--grey-3);
    font-size: 11px;
    line-height: 1.25;
  }
  .contacts {
    list-style: none;
    margin-top: 12px;
  }
  .contacts li {
    display: flex;
    align-items: center;
    height: 25px;
    color: var(--brand-blue);
    font-size: 13.5px;
  }
  .contacts .icon {
    width: 44px;
    display: flex;
    align-items: center;
    gap: 4px;
    flex-shrink: 0;
  }
  .contacts svg { display: block; }
  .social-dot {
    width: 14px; height: 14px; border-radius: 50%;
    background: var(--grey-4);
  }
  .social-sep { color: var(--grey-3); font-size: 11px; }
</style>
</head>
<body>

  <section class="card card-back" aria-label="Card back">
    <div class="back-wordmark">Dravelin</div>
    <div class="back-tagline">Dravelin Consulting Services</div>
  </section>

  <section class="card card-front" aria-label="Card front">
    <div class="front-watermark" aria-hidden="true">Dravelin</div>

    <div class="front-brand">
      <div class="wordmark">Dravelin</div>
      <div class="tagline">Dravelin Consulting Services</div>
    </div>

    <div class="divider"></div>

    <div class="details">
      <h1 class="person-name">Your Name Here</h1>
      <ul class="roles">
        <li>CEO</li>
        <li>ICO Advisor</li>
        <li>World Champion Gamer</li>
        <li>Esports Award Winner</li>
        <li>Quorvane Expert</li>
      </ul>

      <ul class="contacts">
        <li>
          <span class="icon"><span class="social-dot"></span><span class="social-sep">/</span><span class="social-dot"></span></span>
          @yourusername
        </li>
        <li>
          <span class="icon">
            <svg width="16" height="16" viewBox="0 0 24 24" aria-hidden="true"><path fill="none" stroke="#9d9d9d" stroke-width="2" d="M6 3h3l2 5-2 1.5a11 11 0 0 0 5.5 5.5L16 13l5 2v3a2 2 0 0 1-2 2A16 16 0 0 1 4 5a2 2 0 0 1 2-2z"/></svg>
          </span>
          (00) 0000 0000
        </li>
        <li>
          <span class="icon">
            <svg width="16" height="18" viewBox="0 0 16 24" aria-hidden="true"><rect x="3" y="1" width="10" height="22" rx="2" fill="none" stroke="#9d9d9d" stroke-width="1.8"/><line x1="6" y1="19" x2="10" y2="19" stroke="#9d9d9d" stroke-width="1.8"/></svg>
          </span>
          0000 000 000
        </li>
        <li>
          <span class="icon">
            <svg width="16" height="16" viewBox="0 0 24 24" aria-hidden="true"><circle cx="12" cy="12" r="4" fill="none" stroke="#9d9d9d" stroke-width="2"/><path d="M16 8v5a3 3 0 0 0 6 0v-1a10 10 0 1 0-4 8" fill="none" stroke="#9d9d9d" stroke-width="2"/></svg>
          </span>
          youremailaddress@mailbox.com
        </li>
        <li>
          <span class="icon">
            <svg width="16" height="16" viewBox="0 0 24 24" aria-hidden="true"><g fill="none" stroke="#9d9d9d" stroke-width="1.8"><circle cx="12" cy="12" r="10"/><ellipse cx="12" cy="12" rx="4" ry="10"/><line x1="2" y1="12" x2="22" y2="12"/></g></svg>
          </span>
          www.yourwebsite.com
        </li>
      </ul>
    </div>
  </section>

</body>
</html>
```